Birchwell Landing - Multifamily Development

Birchwell Landing is a Luxury Multifamily Development project located in Orange, NJ. This project will be completed in three phases with the first phase about 75% complete. Each phase will have a different name as follows
CREST Birchwell Landing
RIDGE Birchwell Landing
ZENITHAL Birchwell Landing
We are going to install a banner on the side of the first building which will act as advertising for all buildings. We will eventually need advertising that will be in the windows as well as marketing materials . We want the marketing for this project to be similar for all three phases. At the moment, we are starting with this first simple banner. Attached is a rough idea of the look as well as our color palette. If you feel the color palette is a little too monochrome, feel free to propose an accent color. You can also visit our website to see more info on our company as well as the project. www.tolvarhq.com Finally, if you need AI files (ie. for the logo), we can send to you. Thanks..

```html
<!DOCTYPE html>
<html lang="en">
<head>
<meta charset="utf-8">
<title>CREST Birchwell Landing – Luxury Apartment Rentals</title>
<link href="https://fonts.googleapis.com/css2?family=Montserrat:wght@300;400;500;800&family=Marcellus&display=swap" rel="stylesheet">
<style>
  :root {
    --navy: #1b2438;
    --steel-blue: #4a72a8;
    --slate-band: #3d5177;
    --white: #ffffff;
    --sky-top: #8fb0cf;
    --sky-low: #d9e3ea;
    --brick: #9a5a45;
    --street: #6f7377;
  }
  html, body {
    margin: 0;
    padding: 0;
    width: 1200px;
    height: 4598px;
    overflow: hidden;
    background: var(--navy);
  }
  .banner {
    width: 1200px;
    height: 4598px;
    display: flex;
    flex-direction: column;
    color: var(--white);
    font-family: "Montserrat", sans-serif;
    text-align: center;
  }
  .rendering {
    width: 100%;
    flex: none;
  }
  .rendering--corner {
    height: 768px;
    background: linear-gradient(180deg, var(--sky-top) 0%, var(--sky-low) 22%, #b98a6c 40%, var(--brick) 62%, #8a7f74 84%, var(--street) 100%);
  }
  .rendering--street {
    height: 848px;
    background: linear-gradient(180deg, var(--sky-low) 0%, #e6e8ea 14%, #a7685a 34%, #cdc7c0 58%, #8c5446 80%, #9c9fa1 100%);
  }
  .brand-band {
    height: 661px;
    background: var(--steel-blue);
    display: flex;
    flex-direction: column;
    align-items: center;
    justify-content: center;
    gap: 40px;
  }
  .brand-name {
    font-weight: 800;
    font-size: 210px;
    line-height: 0.9;
    letter-spacing: 2px;
  }
  .brand-sub {
    font-weight: 800;
    font-size: 62px;
    letter-spacing: 38px;
    margin-right: -38px;
  }
  .project-band {
    height: 791px;
    display: flex;
    flex-direction: column;
    align-items: center;
    justify-content: center;
  }
  .project-phase {
    font-weight: 800;
    font-size: 300px;
    line-height: 1;
    letter-spacing: -4px;
  }
  .project-name {
    font-weight: 400;
    font-size: 172px;
    line-height: 1.02;
  }
  .offer-band {
    height: 1250px;
    display: flex;
    flex-direction: column;
    align-items: center;
    padding-top: 90px;
    box-sizing: border-box;
  }
  .rule {
    width: 930px;
    height: 40px;
  }
  .offer-title {
    font-family: "Marcellus", serif;
    font-size: 174px;
    line-height: 1.02;
    letter-spacing: 6px;
    margin: 40px 0 30px;
  }
  .call-label {
    font-weight: 300;
    font-size: 150px;
    line-height: 1;
    margin-top: 120px;
  }
  .call-number {
    font-weight: 800;
    font-size: 172px;
    line-height: 1.05;
    letter-spacing: -2px;
  }
  .contact-line {
    display: flex;
    align-items: center;
    justify-content: center;
    font-weight: 500;
    text-shadow: 2px 3px 4px rgba(0,0,0,0.35);
  }
  .contact-line--email {
    height: 141px;
    background: var(--slate-band);
    font-size: 68px;
  }
  .contact-line--web {
    height: 139px;
    background: var(--steel-blue);
    font-size: 84px;
  }
</style>
</head>
<body>
  <main class="banner">
    <div class="rendering rendering--corner" role="img" aria-label="Architectural rendering of a five-storey brick apartment building on a street corner with trees, traffic lights and a passing car"></div>

    <header class="brand-band">
      <div class="brand-name">TOLVAR</div>
      <div class="brand-sub">PROPERTIES</div>
    </header>

    <section class="project-band">
      <div class="project-phase">CREST</div>
      <div class="project-name">BIRCHWELL</div>
      <div class="project-name">LANDING</div>
    </section>

    <div class="rendering rendering--street" role="img" aria-label="Architectural rendering of the apartment building facade in red brick and light panels, with pedestrians on the sidewalk"></div>

    <section class="offer-band">
      <svg class="rule" viewBox="0 0 930 40" aria-hidden="true">
        <line x1="10" y1="28" x2="920" y2="28" stroke="#ffffff" stroke-width="4"/>
        <circle cx="10" cy="28" r="7" fill="none" stroke="#ffffff" stroke-width="4"/>
        <circle cx="920" cy="28" r="7" fill="none" stroke="#ffffff" stroke-width="4"/>
      </svg>
      <h1 class="offer-title" style="font-weight:400">LUXURY<br>APARTMENT<br>RENTALS</h1>
      <svg class="rule" viewBox="0 0 930 40" aria-hidden="true">
        <line x1="10" y1="12" x2="920" y2="12" stroke="#ffffff" stroke-width="4"/>
        <circle cx="10" cy="12" r="7" fill="none" stroke="#ffffff" stroke-width="4"/>
        <circle cx="920" cy="12" r="7" fill="none" stroke="#ffffff" stroke-width="4"/>
      </svg>
      <div class="call-label">CALL US</div>
      <div class="call-number">973-555-0148</div>
    </section>

    <footer>
      <div class="contact-line contact-line--email">Email: rentals@tolvarhq.com</div>
      <div class="contact-line contact-line--web">www.tolvarhq.com</div>
    </footer>
  </main>
</body>
</html>
```